Telecommunications/Power civil contractor needs business card design

Were a new telecommunications/power underground civil contractor that is looking for a new business card design. Our company colours are silver or grey and orange. Feel free to use the white background logo or the black background logo.

Target Market(s)

Local contractors, utility companies, private sector mining/energy companies, developers.

Industry/Entity Type

Telecommunications

Contact Information for Business Card

Each card will need the following info:
Persons name:
Title:
E-mail:
Phone number:
Shop Address:
Mailing Address:

Requirements
Must have
• Each card will need the following info:
• Persons name:
• Title:
• E-mail:
• Phone number:
• Shop Address:
• Mailing Address:

```html
<!DOCTYPE html>
<html lang="en">
<head>
<meta charset="utf-8">
<title>Ridgeline Civil Works – Business Card</title>
<link href="https://fonts.googleapis.com/css2?family=Roboto:wght@400;500;700&display=swap" rel="stylesheet">
<style>
  :root {
    --backdrop: #4a3f3a;
    --card-black: #1c1c1d;
    --ink-white: #f2f2f2;
    --ink-grey: #9a9a9c;
    --accent-orange: #f05a24;
    --rule-grey: #8c8c8e;
  }
  * { margin: 0; padding: 0; box-sizing: border-box; }
  html, body {
    width: 1200px; height: 787px; overflow: hidden;
    background: var(--backdrop);
    font-family: "Roboto", Arial, sans-serif;
  }
  .sheet {
    position: relative; width: 1200px; height: 787px;
    display: flex; align-items: center; justify-content: center; gap: 40px;
  }
  .card {
    position: relative; width: 530px; height: 303px;
    background: var(--card-black);
    border-radius: 3px;
    box-shadow: 0 10px 24px rgba(0,0,0,.45);
  }
  /* front face */
  .card-front { display: flex; align-items: center; justify-content: center; gap: 18px; }
  .front-mark {
    width: 96px; height: 96px; border-radius: 50%;
    border: 5px solid var(--ink-grey);
  }
  .front-name {
    color: var(--ink-grey); font-weight: 700; font-size: 26px;
    letter-spacing: 1px; text-transform: uppercase; line-height: 1.15;
  }
  /* back face */
  .person { position: absolute; left: 40px; top: 54px; }
  .person-name { color: var(--accent-orange); font-size: 21px; font-weight: 500; }
  .person-title { color: var(--ink-white); font-size: 14px; margin-top: 3px; }
  .contact-list { position: absolute; left: 40px; top: 122px; list-style: none; }
  .contact-list li {
    display: flex; align-items: center; gap: 10px;
    color: var(--ink-white); font-size: 14.5px; height: 21px;
  }
  .contact-list svg { width: 13px; height: 13px; fill: var(--accent-orange); }
  .rule { position: absolute; height: 1px; background: var(--rule-grey); }
  .rule-contact { left: 40px; top: 196px; width: 260px; }
  .rule-address { left: 290px; top: 204px; width: 210px; }
  .brand { position: absolute; right: 30px; top: 58px; display: flex; align-items: center; gap: 12px; }
  .brand-mark {
    width: 52px; height: 52px; border-radius: 50%;
    border: 4px solid var(--accent-orange);
  }
  .brand-name {
    color: var(--accent-orange); font-weight: 700; font-size: 19px;
    text-transform: uppercase; line-height: 1.15; letter-spacing: .5px;
  }
  .addresses {
    position: absolute; right: 30px; top: 212px; text-align: right;
    color: var(--ink-white); font-size: 13.5px; line-height: 1.3;
  }
  .address + .address { margin-top: 4px; }
  .address-label { color: var(--accent-orange); font-weight: 500; }
</style>
</head>
<body>
<main class="sheet">
  <section class="card card-front" aria-label="Card front">
    <div class="front-mark"></div>
    <div class="front-name">Ridgeline<br>Civil Works Inc</div>
  </section>

  <section class="card card-back" aria-label="Card back">
    <div class="person">
      <div class="person-name">Mark Ellison</div>
      <div class="person-title">President</div>
    </div>

    <ul class="contact-list">
      <li>
        <svg viewBox="0 0 24 24" aria-hidden="true"><path d="M6.6 10.8a15 15 0 0 0 6.6 6.6l2.2-2.2a1 1 0 0 1 1-.25 11.4 11.4 0 0 0 3.6.57 1 1 0 0 1 1 1V20a1 1 0 0 1-1 1A17 17 0 0 1 3 4a1 1 0 0 1 1-1h3.5a1 1 0 0 1 1 1c0 1.25.2 2.45.57 3.57a1 1 0 0 1-.25 1z"/></svg>
        555 014 7788
      </li>
      <li>
        <svg viewBox="0 0 24 24" aria-hidden="true"><path d="M2 5h20v14H2zm2 2v.5l8 5 8-5V7zm0 2.8V17h16V9.8l-8 5z"/></svg>
        mark@ridgelinecivil.com
      </li>
      <li>
        <svg viewBox="0 0 24 24" aria-hidden="true"><path d="M12 2a10 10 0 1 0 0 20 10 10 0 0 0 0-20zm0 2a8 8 0 0 1 7.4 5H15a14 14 0 0 0-1.6-4.9A8 8 0 0 1 12 4zm-2 .2A12 12 0 0 0 9 9H4.6A8 8 0 0 1 10 4.2zM4 12c0-.7.1-1.3.2-2h4.6a16 16 0 0 0 0 4H4.2c-.1-.7-.2-1.3-.2-2zm6.8-2h2.4a14 14 0 0 1 0 4h-2.4a14 14 0 0 1 0-4zM4.6 15H9a12 12 0 0 0 1 4.8A8 8 0 0 1 4.6 15zm8.8 4.9A14 14 0 0 0 15 15h4.4a8 8 0 0 1-6 4.9zM15.2 14a16 16 0 0 0 0-4h4.6a8 8 0 0 1 0 4z"/></svg>
        www.ridgelinecivil.com
      </li>
    </ul>
    <div class="rule rule-contact"></div>

    <div class="brand">
      <div class="brand-mark"></div>
      <div class="brand-name">Ridgeline<br>Civil Works Inc</div>
    </div>

    <div class="rule rule-address"></div>
    <div class="addresses">
      <div class="address address-shop"><span class="address-label">Shop:</span> 2170 Harbor Creek Road<br>Lakeview, NY 10990</div>
      <div class="address address-mailing"><span class="address-label">Mail:</span> PO Box 418<br>Lakeview, NY 10990</div>
    </div>
  </section>
</main>
</body>
</html>
```